KTLR Unique Letterhead for Financial Services Business

I am looking for a letterhead design to match our branding colours. I do not want to see anything generic that could be created in word, I can do that myself, I am after something with a bit of designer flair. Once completed I will need files in a print ready format (including bleed area).

I have included our logo file and also our new business card design but get creative.

Industry/Entity Type

Financial Services

Font styles to use
Other font styles liked:
• raleway

Colors
00AB8E
00BBA5
67D7C9
C6EFE9
E9F9F6

Requirements
Must have
• Must be consisten with logo branding colours.
Should not have
• Anything generic that I could create myself in word

```html
<!DOCTYPE html>
<html lang="en">
<head>
<meta charset="utf-8">
<title>KTLR Financial Services Letterhead</title>
<link href="https://fonts.googleapis.com/css2?family=Raleway:wght@400&family=Source+Sans+3:wght@400&family=Open+Sans:wght@700&display=swap" rel="stylesheet">
<style>
  :root {
    --backdrop: #e4e4e4;
    --paper: #ffffff;
    --brand-teal: #1a9aa0;
    --brand-deep: #004f6a;
    --ink: #222222;
    --body-ink: #555555;
    --icon-teal: #0f7f8a;
  }
  * { margin: 0; padding: 0; box-sizing: border-box; }
  html, body { width: 1153px; height: 1200px; overflow: hidden; background: var(--backdrop); }
  .letterhead {
    position: absolute; left: 173px; top: 30px;
    width: 807px; height: 1140px;
    background: var(--paper);
    box-shadow: 0 4px 18px rgba(0,0,0,0.18);
    overflow: hidden;
  }
  .brand { position: absolute; left: 76px; top: 129px; display: flex; align-items: center; gap: 10px; }
  .brand-square { width: 26px; height: 26px; background: var(--brand-teal); flex: none; }
  .brand-name { font-family: "Raleway", sans-serif; font-weight: 400; font-size: 18px; color: var(--brand-deep); white-space: nowrap; }
  .header-divider { position: absolute; left: 364px; top: 89px; width: 2px; height: 108px; background: var(--brand-deep); }
  .contact { position: absolute; left: 386px; top: 84px; font-family: "Raleway", sans-serif; font-size: 16px; color: var(--ink); line-height: 19px; }
  .contact-address { margin-bottom: 20px; }
  .contact-line { display: flex; align-items: center; gap: 5px; }
  .contact-line svg { width: 14px; height: 14px; flex: none; }
  .recipient { position: absolute; left: 76px; top: 310px; font-family: "Source Sans 3", sans-serif; color: var(--body-ink); }
  .recipient-name { font-size: 16px; letter-spacing: 0.2px; line-height: 22px; }
  .recipient-line { font-size: 12px; line-height: 20px; }
  .letter-body { position: absolute; left: 76px; top: 404px; width: 653px; font-family: "Source Sans 3", sans-serif; font-size: 12px; line-height: 19.8px; color: var(--body-ink); text-align: justify; }
  .letter-body p { margin-bottom: 17px; }
  .closing { position: absolute; left: 76px; top: 787px; font-family: "Source Sans 3", sans-serif; font-size: 13px; color: var(--body-ink); }
  .signature-mark { position: absolute; left: 76px; top: 824px; width: 98px; height: 14px; background: linear-gradient(90deg, rgba(40,40,40,0.55), rgba(40,40,40,0.2)); border-radius: 7px; }
  .signatory { position: absolute; left: 76px; top: 851px; font-family: "Open Sans", sans-serif; font-weight: 700; font-size: 14px; color: var(--brand-deep); }
  .footer-band { position: absolute; left: 0; bottom: 0; width: 100%; height: 41px; background: var(--brand-deep); }
  .footer-badge { position: absolute; left: 613px; top: 1015px; width: 120px; height: 106px; background: var(--paper); border-radius: 6px 6px 26px 6px; display: flex; align-items: center; justify-content: center; }
  .footer-badge-square { width: 78px; height: 78px; background: linear-gradient(135deg, var(--brand-teal), var(--brand-deep)); border-radius: 4px 4px 20px 4px; }
</style>
</head>
<body>
  <div class="letterhead">
    <div class="brand">
      <div class="brand-square"></div>
      <div class="brand-name">KTLR Financial Services</div>
    </div>

    <div class="header-divider"></div>

    <div class="contact">
      <div class="contact-address">PO Box 4187 Ridgeview<br>NSW 2410</div>
      <div class="contact-line">
        <svg viewBox="0 0 16 16"><path fill="var(--icon-teal)" d="M3.6 1.5l2.2 2.4-1.1 1.7c.8 1.9 2.2 3.3 4.1 4.2l1.7-1.1 2.4 2.2-1.3 2.3C6.5 13 2.9 9.4 2 4.4z"/><path fill="none" stroke="var(--icon-teal)" stroke-width="1.2" d="M9.5 2.5a4 4 0 0 1 4 4M9.5 0.8a5.7 5.7 0 0 1 5.7 5.7"/></svg>
        <span>(802) 555-0192</span>
      </div>
      <div class="contact-line">
        <svg viewBox="0 0 16 16"><rect x="1.5" y="4" width="13" height="9" fill="var(--icon-teal)"/><path d="M1.5 4l6.5 5 6.5-5" fill="none" stroke="#fff" stroke-width="1.2"/></svg>
        <span>info@ktlrfinancialservices.com.au</span>
      </div>
      <div class="contact-line">
        <svg viewBox="0 0 16 16"><circle cx="8" cy="8" r="6.5" fill="var(--icon-teal)"/><path d="M4 5.5c1.5.2 2.5 1 2.2 2.3-.3 1.2 1 1.7 1.2 3.2M10 3.2c-.5 1.3.5 2 1.8 2.2M9.5 9.5c1 .2 2 .8 2.4 1.8" fill="none" stroke="#fff" stroke-width="1"/></svg>
        <span>www.ktlrfinancialservices.com.au</span>
      </div>
    </div>

    <div class="recipient">
      <div class="recipient-name">ELISE HARROW</div>
      <div class="recipient-line">Chief Exective Officer</div>
      <div class="recipient-line">City/State, Zip Code</div>
    </div>

    <div class="letter-body">
      <p>Proin gravida nibh vel velit auctor aliquet. Aenean sollicitudin, lorem quis bibendum auctor, nisi elit consequat ipsum, nec sagittis sem nibh id elit. Duis sed odio sit amet nibh vulputate cursus a sit amet mauris. Morbi accumsan ipsum velit. Nam nec tellus a odio tincidunt auctor a ornare odio. Sed non mauris vitae erat consequat auctor eu in elit. Class aptent taciti sociosqu ad litora torquent ugue. Sed non neque elit. Sed ut imperdiet nisi. Proin condimentum fermentum nunc. Etiam pharetra, imperdiet nisi. Proin condimentum fermentum nunc. Etiam pharetra, erat sed fermentum feugiat, velit mauris egestas quam, ut aliquam massa nisl quis neque. Suspendisse in orci enim.</p>
      <p>This is the studio's version of Lorem Ipsum. Proin gravida nibh vel velit auctor aliquet. Aenean sollicitudin, lorem quis bibendum auctor, nisi elit consequat ipsum, nec sagittis sem nibh id elit. Duis sed odio sit amet nibh vulputate cursus a sit amet mauris. Mo rbi accumsan ipsum velit. Nam nec tellus a odio tincidunt auctor a ornare odio. Sed non mauris vitae erat consequat auctor eu in elit. Class aptt consequat auctor eu in elit. Class aptent taciti sociosqu ad litora torquent per conubia nostra, per inceptos himenaeos. Mauris in erat justo.</p>
      <p>Nullam ac urna eu felis dapibus condimentum sit amet a augue. Sed non neque elit. Sed ut imperdiet nisi. Proin condimentum fermentum nunc. Etiam pharetra, erat sed fermentum feugiat, velit mauris egestas quam.Nullam ac urna eu felis dapibus condimentum sit amet a aug pharetra, erat sed fermentum feugiat, velit mauris egestas quam.Nullam ac urna eu felis dapibus condimentum sit amet a augue. Sed non neque elit. Sed ut imperdiet nisi. Proin condimentum fermentum nunc.</p>
    </div>

    <div class="closing">Sincerely,</div>
    <div class="signature-mark" role="img" aria-label="Handwritten signature of Daniel Okafor"></div>
    <div class="signatory">Daniel Okafor</div>

    <div class="footer-band"></div>
    <div class="footer-badge"><div class="footer-badge-square"></div></div>
  </div>
</body>
</html>
```